Turm7Zwerge
Zielgruppe
Zielgruppe sind die Eltern, Lehrer, Kindergärtner, aber auch Kinder, die bereits Lesen können.
Aufgabenstellung
Ich brauche einen Flyer und ein Plakat für eine Kinderschachschule für Kinder zwischen 4 und 15 Jahren. Auf dem Flyer, den ich in A6-Format drucken möchte (beidseitig), muss ich die Info über die Kinderschachschule Turm7Zwerge (mehr Infos unter www.turm7zwerge-beispiel.ch), dh., was wir machen, Kontaktdaten, etc schreiben können. Es dient als Werbematerial zum Auslegen
Auf dem Plakat wird mehr oder weniger das Gleiche stehen, es wird jedoch als Din A4 Seite aufgehängt.
Unsere Kontaktinformation ist wie folgt:
Turm7Zwerge: Spielen mit kleinen Strategen
www.turm7zwerge-beispiel.ch

```html
<!DOCTYPE html>
<html lang="de">
<head>
<meta charset="utf-8">
<title>Turm7Zwerge – Plakat</title>
<link rel="stylesheet" href="https://fonts.googleapis.com/css2?family=Nunito:wght@800;900&family=Oswald:wght@600;700&family=Arimo:wght@400;700&display=swap">
<style>
  :root {
    --magenta: #c8267f;
    --magenta-dark: #a51c69;
    --blue: #2f8fd0;
    --orange: #f2a12b;
    --red: #e2343c;
    --green: #7bb33a;
    --ink: #1a1a1a;
    --white: #ffffff;
    --paper: #ffffff;
  }
  * { margin: 0; padding: 0; box-sizing: border-box; }
  html, body { width: 855px; height: 1200px; overflow: hidden; background: var(--paper); }
  .poster { position: relative; width: 855px; height: 1200px; overflow: hidden; background: var(--paper); font-family: "Arimo", Arial, sans-serif; }

  .claim { position: absolute; left: 50px; top: 52px; font-family: "Nunito", Arial, sans-serif; font-weight: 900; font-size: 36px; line-height: 54px; letter-spacing: 0; white-space: nowrap; }
  .claim .c1 { color: var(--red); }
  .claim .c2 { color: var(--orange); }
  .claim .c3 { color: var(--green); }
  .claim .c4 { color: var(--blue); }
  .claim .c5 { color: var(--magenta); }

  .brand { position: absolute; left: 600px; top: 108px; display: flex; align-items: center; gap: 8px; }
  .brand-mark { width: 18px; height: 18px; background: var(--magenta); }
  .brand-name { font-family: "Nunito", Arial, sans-serif; font-weight: 900; font-size: 28px; line-height: 1; color: var(--magenta); white-space: nowrap; }

  .stripes { position: absolute; left: 0; width: 855px; }
  .stripes span { display: block; }
  .stripes .s-mag { height: 6px; background: var(--magenta); }
  .stripes .s-gap { height: 3px; background: var(--white); }
  .stripes .s-blue { height: 5px; background: var(--blue); }
  .stripes .s-orange { height: 5px; background: var(--orange); }
  .stripes--top { top: 190px; }
  .stripes--bottom { top: 1016px; }

  .board-backdrop { position: absolute; left: 0; top: 212px; width: 855px; height: 800px;
    background: linear-gradient(180deg, #f4f4f4 0%, #ffffff 40%, #f2f2f2 100%); }

  .slogans { position: absolute; left: 0; top: 228px; font-family: "Oswald", Impact, sans-serif; font-weight: 700; font-size: 50px; line-height: 64px; color: var(--ink); }
  .slogans p { position: relative; white-space: nowrap; }
  .slogans .l1 { left: 140px; text-shadow: 0 0 6px rgba(200,38,127,.55), 0 0 2px var(--white); }
  .slogans .l2 { left: 190px; text-shadow: 0 0 6px rgba(242,161,43,.7), 0 0 2px var(--white); }
  .slogans .l3 { left: 255px; text-shadow: 0 0 6px rgba(47,143,208,.7), 0 0 2px var(--white); }

  .offer { position: absolute; left: 245px; top: 420px; color: var(--ink); }
  .offer h2 { font-family: "Arimo", Arial, sans-serif; font-weight: 700; font-size: 25px; margin-bottom: 8px; }
  .offer ul { list-style: none; font-size: 22px; line-height: 32px; }
  .offer li::before { content: "• "; }
  .offer li:nth-child(1) { margin-left: 12px; }
  .offer li:nth-child(2) { margin-left: 40px; }
  .offer li:nth-child(3) { margin-left: 70px; }
  .offer li:nth-child(4) { margin-left: 95px; }
  .offer li:nth-child(5) { margin-left: 120px; }

  .photo { position: absolute; left: 30px; top: 615px; width: 825px; height: 398px;
    background: linear-gradient(120deg, #e9d2b4 0%, #c9a37a 45%, #8a6642 75%, #3a2c22 100%); }

  .footer { position: absolute; left: 0; top: 1040px; width: 855px; height: 160px;
    background: linear-gradient(180deg, var(--magenta) 0%, var(--magenta-dark) 100%); }
  .contact { position: absolute; left: 40px; top: 30px; color: var(--white); font-size: 17px; line-height: 27px; font-style: normal; white-space: nowrap; }
  .pieces { position: absolute; left: 700px; top: 28px; width: 128px; height: 112px;
    background: linear-gradient(90deg, #ffffff 0%, #f2a12b 35%, #2f8fd0 65%, #1a1a1a 100%); opacity: .9; }
</style>
</head>
<body>
<main class="poster">
  <h1 class="claim">
    <span class="c1">WIR </span><span class="c2">BRINGEN </span><span class="c3">IHR </span><span class="c4">KIND</span><br>
    <span class="c5">ZUG </span><span class="c1">UM </span><span class="c2">ZUG </span><span class="c3">ZUM </span><span class="c4">ERFOLG!</span>
  </h1>

  <div class="brand">
    <span class="brand-mark"></span>
    <span class="brand-name">Turm7Zwerge</span>
  </div>

  <div class="stripes stripes--top"><span class="s-mag"></span><span class="s-gap"></span><span class="s-blue"></span><span class="s-gap"></span><span class="s-orange"></span></div>

  <div class="board-backdrop"></div>

  <div class="photo" role="img" aria-label="Foto: Mädchen hält eine schwarze Königsfigur hoch, daneben ein Schachbrett mit Holzfiguren"></div>

  <div class="slogans">
    <p class="l1">SCHACH MACHT SPASS!</p>
    <p class="l2">SCHACH MACHT SCHLAU!</p>
    <p class="l3">SCHACH MACHT STARK!</p>
  </div>

  <section class="offer">
    <h2>Wir bieten Ihrem Kind:</h2>
    <ul>
      <li>Konzentrationstraining</li>
      <li>Intellektuelle Förderung</li>
      <li>Stärkung des Selbstvertrauens</li>
      <li>Persönliches Wachstum</li>
      <li>Spass und Spannung</li>
    </ul>
  </section>

  <div class="stripes stripes--bottom"><span class="s-mag"></span><span class="s-gap"></span><span class="s-blue"></span><span class="s-gap"></span><span class="s-orange"></span><span class="s-gap"></span></div>

  <footer class="footer">
    <address class="contact">
      Turm7Zwerge: Spielen mit kleinen Strategen<br>
      Lena Brunner, Präsidentin<br>
      Lindenweg 12 • Postfach 100 • 8000 Musterdorf<br>
      Tel. 079 000 12 34 • info@turm7zwerge-beispiel.ch • www.turm7zwerge-beispiel.ch
    </address>
    <div class="pieces" role="img" aria-label="Illustration: Schachfiguren Turm, Läufer und Springer in Weiss, Orange, Blau und Schwarz"></div>
  </footer>
</main>
</body>
</html>
```